Web re-design project for web software development agency

We need to re-design our existing website (www.tovenmedia.co.uk), and are going to start using a shorter domain (www.toven.com).
We have been in business for 8 years and it's time for an update.

We are based at Harrowmede Court (home of the code breakers). We specialise in writing software for the web. Over the years we have built up a healthy customer base and it is time to incorporate the features we build for our customers into our own site (e.g. social media).

We have a team of 8 talented developers with varied skills including: apps for mobile; complex server side software; front-end software; eCommerce software; specialised web based applications; integration software; hardware support; consultancy services. Our customers are diverse (e.g. banking; commerce; veterinary; R&D; health sector; law; accounting; film industry etc.).

Our current colour scheme is blue, white and green although we are not averse to moving away from these colours. We will also be dropping the DESIGN from our name and logo. Revised logo will be attached.

The site needs to be modern, sophisticated and leading edge. We want to show visitors to the site that we are a professional organisation.
Updates

Our logo in PSD format has been uploaded. Please drop the word DESIGN from the logo.

The deliverable for this project is a PSD (ideally we would like to see how the home page, portfolio page, resources page with mugshots, and forms are going to look).

Many thanks,
Tom

Please DO NOT include a Careers section 

We will also need a "meet our team" section with spaces for 10 photographs as well as some space underneath them so that we can add a short paragraph for each one of them.

Target Market(s)

Mainly large corporations needing bespoke web software, or generally complex projects (for anyone).

Industry/Entity Type

Software

Requirements
Must have
• We would like a home page designed that has the following elements on it:
- Show the new cookie compliance policy displayed probably in the top of the page (will disappear).
- A client Testimonial.
- Pricing icon.
- Social media Links.
- A Quote section in expand/collapse field as in (http://www.quillbrook-online.co.uk/our-services.shtml)

We would also like a portfolio page that showcases our clients in an interesting way.

Finally, we would like a form design that we can use throughout the site (i.e. how should buttons, radio buttons, checkboxes, dropdowns, text areas etc. look)?
Nice to have
• A page that follows these guidelines:
http://www.pagerivet.com/the-anatomy-of-a-perfect-landing-page

Here are a few examples of sites in our sector that we like:
- http://www.tidewell-studio.com/
- http://plinthos.co.uk/
- http://www.fernaxis.com/services/web-development (nice contact us page)
- http://www.quillbrook-online.co.uk/
- http://www.lumsa.com/
- http://www.netmoxa.co.uk/
Should not have
• No flash elemets. If anything, we will use html5.

```html
<!DOCTYPE html>
<html lang="en">
<head>
<meta charset="utf-8">
<title>Toven – Web Software Development</title>
<link rel="stylesheet" href="https://fonts.googleapis.com/css2?family=Arimo:wght@400;700&family=PT+Sans:wght@400;700&family=Questrial&display=swap">
<style>
:root{
  --page:#eef0f2;
  --header:#f5f6f7;
  --ink:#333;
  --muted:#555;
  --navy:#1f3f74;
  --lime:#a8c416;
  --lime-btn:#bfd62a;
  --dark:#1a1a1a;
  --rule:#d8dadc;
  --link:#2a5a9a;
  --social:#2a6fb0;
}
*{margin:0;padding:0;box-sizing:border-box}
html,body{width:1061px;height:1200px;overflow:hidden}
body{background:var(--page);font-family:Arimo,Arial,sans-serif;color:var(--ink);position:relative}
.abs{position:absolute}

.cookie-bar{left:0;top:0;width:1061px;height:37px;background:linear-gradient(#2b2b2b,#0c0c0c);color:#fff;font-size:10.5px;display:flex;align-items:center}
.cookie-bar p{position:absolute;left:110px}
.cookie-bar .dismiss{position:absolute;left:760px;top:8px;width:75px;height:22px;background:linear-gradient(#f6f6f6,#cfcfcf);color:#222;border-radius:3px;font-size:12px;display:flex;align-items:center;justify-content:center}
.cookie-bar .what{position:absolute;left:859px}

.site-header{left:0;top:37px;width:1061px;height:111px;background:var(--header);border-bottom:1px solid #e0e2e4}
.brand{left:98px;top:59px;display:flex;align-items:center;gap:10px}
.brand .mark{width:30px;height:30px;background:var(--lime)}
.brand .name{font-family:'PT Sans',sans-serif;font-weight:700;font-size:34px;color:var(--navy);letter-spacing:1px}
.quote-btn{left:802px;top:37px;width:161px;height:28px;background:#0d0d0d;color:#fff;font-family:'PT Sans',sans-serif;font-weight:700;font-size:20px;display:flex;align-items:center;justify-content:center;border-radius:0 0 4px 4px}
.call{left:760px;top:72px;width:203px;text-align:right;font-family:Questrial,sans-serif;font-size:10px;color:#333}
.call span{color:#8aa80d}
.main-nav{left:455px;top:89px;width:508px;height:33px;background:linear-gradient(#4a4a4a,#111);border-radius:3px;display:flex}
.main-nav a{flex:1;color:#fff;font-family:Questrial,sans-serif;font-size:10.5px;text-decoration:none;display:flex;align-items:center;justify-content:center;border-right:1px solid #000;box-shadow:1px 0 0 #555;white-space:nowrap}
.main-nav a:last-child{border:0;box-shadow:none}

.hero-frame{left:103px;top:177px;width:855px;height:398px;background:#fff;box-shadow:0 0 4px rgba(0,0,0,.12)}
.hero-img{left:112px;top:186px;width:836px;height:380px;background:radial-gradient(ellipse 120px 160px at 640px 190px,rgba(230,130,30,.55),transparent 70%),radial-gradient(ellipse 240px 260px at 600px 230px,#4a4c50,transparent 75%),linear-gradient(100deg,#151b22 0%,#222830 55%,#1a1d22 100%)}
.hero-line{left:112px;top:312px;width:836px;height:1px;background:linear-gradient(90deg,transparent,rgba(170,200,230,.6),transparent)}
.hero-copy{left:138px;top:310px;color:#fff;font-family:'PT Sans',sans-serif}
.hero-copy h1{font-size:52px;font-weight:400;line-height:1;letter-spacing:-.5px}
.hero-copy p{font-size:21px;margin-top:10px}
.hero-copy .learn{display:inline-block;margin-top:12px;background:var(--lime-btn);color:#222;font-size:12.5px;padding:4px 8px;border-radius:3px;border:1px solid #e6f08a}

.feature{top:598px;width:290px;height:112px}
.feature .icon{position:absolute;left:8px;top:4px;width:68px;height:64px;border-radius:6px}
.feature h3{position:absolute;left:88px;top:6px;color:var(--lime);font-size:13.5px;font-weight:700}
.feature h4{position:absolute;left:88px;top:22px;font-weight:400;font-size:13px;color:#333}
.feature p{position:absolute;left:88px;top:42px;width:168px;font-size:10.5px;line-height:13px;color:#555;text-align:justify}
.pill{position:absolute;left:8px;top:91px;background:var(--navy);color:#fff;font-size:11.5px;padding:3px 8px;border-radius:10px}
.vrule{width:1px;background:var(--rule)}

.bar-head{height:30px;background:linear-gradient(#3a3a3a,#0e0e0e);color:#fff;font-weight:700;font-size:14px;display:flex;align-items:center;padding-left:13px;letter-spacing:.3px}
.clients{left:97px;top:770px;width:265px;font-size:10.5px;line-height:13px;color:#444}
.clients .date{font-weight:700;color:#333;margin-bottom:4px}
.clients .who{font-weight:700;font-style:italic;margin:3px 0 13px}
.dark-btn{background:#1a1a1a;color:#fff;font-size:10.5px;padding:5px 5px;border-radius:3px;display:inline-block}
.spec-intro{left:400px;top:774px;width:560px;font-size:10.5px;line-height:13px;color:#444}
.spec{width:290px;height:70px}
.spec .icon{position:absolute;left:3px;top:4px;width:46px;height:46px;border-radius:8px}
.spec h3{position:absolute;left:56px;top:0;color:var(--navy);font-size:13.5px;font-weight:700}
.spec p{position:absolute;left:56px;top:17px;width:212px;font-size:10.5px;line-height:13px;color:#444}
.spec a{position:absolute;left:56px;top:43px;font-size:10px;color:var(--link)}

.hrule{height:1px;background:var(--rule)}
.client-name{top:1052px;font-family:Arimo,Arial,sans-serif;font-weight:700;font-size:18px;color:#555;display:flex;align-items:center;gap:8px;height:36px;white-space:nowrap}
.client-name i{display:inline-block;width:12px;height:12px;background:#555}

.badge{top:1160px;width:78px;height:25px;background:#dce4ee;border:1px solid #9aaec6}
.legal{left:600px;top:1153px;width:363px;text-align:right;font-size:9.5px;color:#444}
.social{top:1168px;width:22px;height:22px;background:var(--social);border-radius:2px}
.foot-links{left:892px;top:1178px;font-size:9.5px;color:#444}
</style>
</head>
<body>

<div class="abs cookie-bar">
  <p>We'd like to set optional cookies to make your user experience better, by using this site you give your consent for us to do this.</p>
  <span class="dismiss">Dismiss</span>
  <span class="what">What are cookies?</span>
</div>

<header class="abs site-header"></header>
<div class="abs brand"><span class="mark"></span><span class="name">TOVEN</span></div>
<div class="abs quote-btn">Get a quote</div>
<div class="abs call">Call us now: <span>+1(555)01-23-45</span></div>
<nav class="abs main-nav">
  <a href="#">Home</a><a href="#">About Us</a><a href="#">Our Services</a><a href="#">Technology</a><a href="#">Portfolio</a><a href="#">Contact Us</a>
</nav>

<div class="abs hero-frame"></div>
<div class="abs hero-img" role="img" aria-label="Businessman touching a glowing shopping cart icon surrounded by floating sale badges"></div>
<div class="abs hero-line"></div>
<div class="abs hero-copy">
  <h1>Effective Soft.</h1>
  <p>Looking beyond the possible</p>
  <span class="learn">Learn More</span>
</div>

<section class="abs feature" style="left:97px">
  <div class="icon" role="img" aria-label="Pen on a paper form" style="background:linear-gradient(#fafafa,#d8dde2)"></div>
  <h3>Our Services</h3><h4>What can we do for you?</h4>
  <p>Lorem Ipsum is simply dummy text of the printing and typesetting industry. Lorem Ipsum has been the industry's.</p>
  <span class="pill">Find More</span>
</section>
<div class="abs vrule" style="left:378px;top:592px;height:118px"></div>
<section class="abs feature" style="left:399px">
  <div class="icon" role="img" aria-label="Robotic walking machines in yellow and black" style="background:linear-gradient(#e8e4b0,#9a9a9a)"></div>
  <h3>The Technology</h3><h4>What can we do for you?</h4>
  <p>Lorem Ipsum is simply dummy text of the printing and typesetting industry. Lorem Ipsum has been the industry's.</p>
  <span class="pill">Find More</span>
</section>
<div class="abs vrule" style="left:679px;top:592px;height:118px"></div>
<section class="abs feature" style="left:700px">
  <div class="icon" role="img" aria-label="Brown leather briefcase" style="background:linear-gradient(#c4683a,#7a3414)"></div>
  <h3>Our Work</h3><h4>What can we do for you?</h4>
  <p>Lorem Ipsum is simply dummy text of the printing and typesetting industry. Lorem Ipsum has been the industry's.</p>
  <span class="pill">Find More</span>
</section>

<div class="abs bar-head" style="left:97px;top:735px;width:258px">What Clients say</div>
<div class="abs clients">
  <p class="date">21-05-2012</p>
  <p>Lorem Ipsum is simply dummy text of the printing and typesetting industry. Lorem Ipsum has been the industry's standard dummy text.1960s with the release of Letraset sheets.</p>
  <p class="who">Customer Name</p>
  <p class="date">21-05-2012</p>
  <p>Lorem Ipsum is simply dummy text of the printing and typesetting industry. Lorem Ipsum has been the industry's standard dummy text.</p>
  <p class="who">Customer Name</p>
  <span class="dark-btn" style="margin-top:8px">Read More</span>
</div>
<div class="abs vrule" style="left:378px;top:772px;height:216px"></div>

<div class="abs bar-head" style="left:399px;top:735px;width:564px">Our Specialization</div>
<p class="abs spec-intro">Lorem Ipsum is simply dummy text of the printing and typesetting industry. Lorem Ipsum has been the industry's standard dummy text ever since the 1500s.</p>
<section class="abs spec" style="left:400px;top:811px">
  <div class="icon" role="img" aria-label="Cup of brushes and pencils" style="background:linear-gradient(#c9d6e4,#6d8fb5)"></div>
  <h3>Design</h3><p>Graphic design for a professional website presence...</p><a href="#">Read More</a>
</section>
<section class="abs spec" style="left:692px;top:811px">
  <div class="icon" role="img" aria-label="Gears and wrench" style="background:linear-gradient(#e8e2a0,#8a8a8a)"></div>
  <h3>Development</h3><p>Graphic design for a professional website presence...</p><a href="#">Read More</a>
</section>
<section class="abs spec" style="left:400px;top:889px">
  <div class="icon" role="img" aria-label="Green alarm clock" style="background:linear-gradient(#b8c8d2,#4c7a5a)"></div>
  <h3>Project Management</h3><p>Graphic design for a professional website presence...</p><a href="#">Read More</a>
</section>
<section class="abs spec" style="left:692px;top:889px">
  <div class="icon" role="img" aria-label="Yellow light bulb" style="background:linear-gradient(#ffd84a,#d89a10)"></div>
  <h3>IT Solutions</h3><p>Graphic design for a professional website presence...</p><a href="#">Read More</a>
</section>
<span class="abs dark-btn" style="left:457px;top:957px">Find More</span>

<div class="abs hrule" style="left:97px;top:1004px;width:866px"></div>
<div class="abs client-name" style="left:105px"><i></i>Lumera</div>
<div class="abs client-name" style="left:268px">AurumVault</div>
<div class="abs client-name" style="left:482px">Pellworth Animal Health</div>
<div class="abs client-name" style="left:775px">Rattlebox Records</div>

<div class="abs hrule" style="left:97px;top:1146px;width:866px"></div>
<div class="abs badge" style="left:100px" role="img" aria-label="Markup validation badge"></div>
<div class="abs badge" style="left:181px" role="img" aria-label="Stylesheet validation badge"></div>
<p class="abs legal">© Toven Ltd. 2012 Registered in England &amp; Wales Number: 04418290.</p>
<div class="abs social" style="left:807px" role="img" aria-label="Professional network link"></div>
<div class="abs social" style="left:834px" role="img" aria-label="Social network link"></div>
<div class="abs social" style="left:861px;background:#5fb0e4" role="img" aria-label="Microblog link"></div>
<p class="abs foot-links">sitemap &nbsp;|&nbsp; login</p>

</body>
</html>
```